Swift Scholars Institute by graduating students from college in two years

Based on the logo design, create stationary and business cards for
Dr. Velimir T Osunde, CEO, (555) 482-1630
and Mirela Thorpe, Respresentative, (301) 557-2048
Address: 4417 Marbleton Lane, Brenwick Station, KS 22061
Incorporate elelments of the logo

Target Market(s)

USA

Other font styles liked:
• match with the logo type style

```html
<!DOCTYPE html>
<html lang="en">
<head>
<meta charset="utf-8">
<title>Swift Scholars Institute — Stationery</title>
<link rel="stylesheet" href="https://fonts.googleapis.com/css2?family=Libre+Baskerville:wght@400;700&family=Inter:wght@400;600&display=swap">
<style>
  :root {
    --navy: #1a2468;
    --navy-deep: #0f1547;
    --gold: #c9a21c;
    --paper: #ffffff;
    --backdrop: #d9dadd;
    --ink: #1c1c28;
    --faint: #e6e7eb;
  }
  * { box-sizing: border-box; margin: 0; padding: 0; }
  html, body { width: 1200px; height: 900px; overflow: hidden; }
  body {
    background: var(--backdrop);
    font-family: "Inter", Arial, sans-serif;
    position: relative;
  }
  .brand-name {
    font-family: "Libre Baskerville", Georgia, serif;
    font-weight: 700;
    text-transform: uppercase;
    letter-spacing: 0.04em;
    line-height: 1.15;
  }
  .brand-mark { border-radius: 50%; flex: none; background: var(--gold); }

  /* Letterhead */
  .letterhead {
    position: absolute; left: 60px; top: 60px;
    width: 480px; height: 680px;
    background: var(--paper);
    box-shadow: 0 12px 30px rgba(0,0,0,0.12);
    overflow: hidden;
  }
  .letterhead-header {
    position: absolute; left: 36px; top: 36px;
    display: flex; align-items: center; gap: 14px;
  }
  .letterhead-header .brand-mark { width: 48px; height: 48px; }
  .letterhead-header .brand-name { color: var(--navy); font-size: 17px; }
  .letterhead-watermark {
    position: absolute; left: 0; top: 380px; width: 480px;
    text-align: center; color: var(--faint); font-size: 24px;
  }
  .letterhead-footer { position: absolute; left: 0; bottom: 0; width: 480px; height: 130px; }
  .letterhead-address {
    position: absolute; right: 30px; bottom: 22px;
    font-family: "Libre Baskerville", Georgia, serif;
    color: #fff; font-size: 13px;
  }

  /* Envelope */
  .envelope {
    position: absolute; left: 600px; top: 60px;
    width: 540px; height: 270px;
    background: var(--navy);
    box-shadow: 0 12px 30px rgba(0,0,0,0.15);
    overflow: hidden;
  }
  .envelope-flap { position: absolute; inset: 0; }
  .envelope-sender {
    position: absolute; left: 30px; bottom: 28px;
    display: flex; align-items: center; gap: 12px;
  }
  .envelope-sender .brand-mark { width: 36px; height: 36px; }
  .envelope-sender .brand-name { color: #fff; font-size: 13px; }

  /* Business cards */
  .business-card {
    position: absolute; left: 600px;
    width: 400px; height: 229px;
    box-shadow: 0 12px 30px rgba(0,0,0,0.15);
    overflow: hidden;
  }
  .card-front { top: 370px; background: var(--paper); }
  .card-back {
    top: 630px; background: var(--navy);
    display: flex; align-items: center; justify-content: center; gap: 16px;
  }

  .card-details { position: absolute; left: 28px; top: 34px; width: 230px; }
  .card-name {
    font-family: "Libre Baskerville", Georgia, serif;
    font-weight: 700; color: var(--navy); font-size: 17px;
  }
  .card-title { font-size: 11px; color: var(--ink); margin-top: 4px; letter-spacing: 0.06em; }
  .card-contact { list-style: none; margin-top: 26px; }
  .card-contact li {
    display: flex; align-items: flex-start; gap: 8px;
    font-size: 10.5px; color: var(--ink); line-height: 1.45; margin-bottom: 8px;
  }
  .card-contact svg { width: 12px; height: 12px; flex: none; margin-top: 2px; }

  .card-strip {
    position: absolute; right: 0; top: 0; width: 120px; height: 100%;
    background: var(--navy);
    border-left: 6px solid var(--gold);
    display: flex; flex-direction: column; align-items: center; justify-content: center; gap: 12px;
  }
  .card-strip .brand-mark { width: 44px; height: 44px; }
  .card-strip .brand-name { color: #fff; font-size: 9.5px; text-align: center; }

  .card-back .brand-mark { width: 60px; height: 60px; }
  .card-back .brand-name { color: #fff; font-size: 16px; }
</style>
</head>
<body>

  <section class="letterhead" aria-label="Letterhead">
    <header class="letterhead-header">
      <span class="brand-mark"></span>
      <span class="brand-name">Swift Scholars<br>Institute</span>
    </header>
    <p class="letterhead-watermark brand-name" aria-hidden="true">Swift Scholars<br>Institute</p>
    <svg class="letterhead-footer" viewBox="0 0 480 130" aria-hidden="true">
      <path d="M0 20 C160 70 320 70 480 60 L480 130 L0 130 Z" fill="var(--gold)"/>
      <path d="M0 34 C160 82 320 82 480 72 L480 130 L0 130 Z" fill="var(--navy)"/>
    </svg>
    <p class="letterhead-address">4417 Marbleton Lane, Brenwick Station, KS 22061</p>
  </section>

  <section class="envelope" aria-label="Envelope">
    <svg class="envelope-flap" viewBox="0 0 540 270" aria-hidden="true">
      <path d="M0 0 L270 140 L540 0" fill="none" stroke="var(--navy-deep)" stroke-width="3"/>
    </svg>
    <div class="envelope-sender">
      <span class="brand-mark"></span>
      <span class="brand-name">Swift Scholars Institute</span>
    </div>
  </section>

  <section class="business-card card-front" aria-label="Business card front">
    <div class="card-details">
      <p class="card-name">Dr. Velimir T Osunde</p>
      <p class="card-title">CEO</p>
      <ul class="card-contact">
        <li>
          <svg viewBox="0 0 24 24"><path fill="var(--navy)" d="M6.6 10.8a15 15 0 006.6 6.6l2.2-2.2a1 1 0 011-.25 11.4 11.4 0 003.6.57 1 1 0 011 1V20a1 1 0 01-1 1A17 17 0 013 4a1 1 0 011-1h3.5a1 1 0 011 1c0 1.25.2 2.45.57 3.57a1 1 0 01-.25 1z"/></svg>
          (555) 482-1630
        </li>
        <li>
          <svg viewBox="0 0 24 24"><path fill="var(--navy)" d="M12 2a7 7 0 00-7 7c0 5.25 7 13 7 13s7-7.75 7-13a7 7 0 00-7-7zm0 9.5A2.5 2.5 0 1112 6.5a2.5 2.5 0 010 5z"/></svg>
          4417 Marbleton Lane, Brenwick Station,<br>KS 22061
        </li>
      </ul>
    </div>
    <div class="card-strip">
      <span class="brand-mark"></span>
      <span class="brand-name">Swift Scholars<br>Institute</span>
    </div>
  </section>

  <section class="business-card card-back" aria-label="Business card back">
    <span class="brand-mark"></span>
    <span class="brand-name">Swift Scholars<br>Institute</span>
  </section>

</body>
</html>
```